Mortgage Company ready to make a statement!

We have a basic logo that I am fairly happy with ... but it could use a little bit of tweaking before we order the sign for our building. We also want some knock-your-socks-off business cards.
Problem: Inside of our Mortgage Office (Brindle Oak Mortgage Group), we are going to have a coffee lounge (Mapleburr Cafe) for Realtors to use instead of the local Quillmont to meet with homebuyers. The office and coffee lounge are in an industrial building and is decorated with cozy overstuffed chairs, a hodge podge of interesting lamps and furniture, and goal is to make it as inviting as possible. However, we are a financial institution... so we need to keep it pretty clean as well.
One of my favorite marketing ideas is to cut a house key for everyone who buys a home using us with a key that matches our logo. There's only one key shape that works really well, so that needs to match the logo in order for the idea to work. I'll attach an image of the key blank.... although the way the key hole cut out looks terrible, so I was thinking of having them just do a thin outline instead.
Would like a similar, matching logo for the Mapleburr Cafe... but possibly something that would be a little less formal and would be cute on a coffee mug- nothing stuffy.
AND, we're opening a home inspection company as well, and we would like that logo and branding to match. The home inspection company is "Brindle Oak Home Inspections"
We were thinking that for the home inspection company , we could use a magnifying glass shape inside of the house shape for the logo, use a keyhole shape inside of the same house for the mortgage company, and use a coffee cup inside of the house shape for Mapleburr Cafe.
Just getting stuck and need to help. I designed the attached logo myself, and that is what we are currently using. Designers at local printing companies have failed to impress us.
The mortgage industry has a lot of numbers and logos, etc that they require us to put on our business cards... so it's hard to keep them looking clean.
HELP! HELP! :)

```html
<!DOCTYPE html>
<html lang="en">
<head>
<meta charset="utf-8">
<title>Brindle Oak Mortgage Group – Business Card</title>
<link href="https://fonts.googleapis.com/css2?family=Open+Sans:wght@700&family=Questrial&display=swap" rel="stylesheet">
<style>
  :root {
    --backdrop: #2b2b2b;
    --card-paper: #f3f3f2;
    --brand-blue: #246583;
    --band-blue: #4f7f95;
    --text-grey: #4a4a4a;
    --rule-grey: #9a9a9a;
  }
  * { margin: 0; padding: 0; box-sizing: border-box; }
  html, body { width: 1200px; height: 960px; overflow: hidden; }
  body {
    background: var(--backdrop);
    position: relative;
    font-family: "Questrial", "Century Gothic", sans-serif;
  }
  .card {
    position: absolute;
    width: 600px;
    height: 343px;
  }
  .card-front { left: 314px; top: 113px; background: var(--card-paper); }
  .card-back { left: 311px; top: 472px; background: var(--brand-blue); }

  .wordmark {
    position: absolute;
    display: flex;
    align-items: center;
    gap: 12px;
    font-family: "Questrial", "Century Gothic", sans-serif;
  }
  .wordmark-square { width: 26px; height: 26px; flex: none; }
  .wordmark-name { line-height: 1.05; letter-spacing: 0.5px; }
  .wordmark-name .line-main { display: block; font-size: 29px; }
  .wordmark-name .line-sub { display: block; font-size: 18px; }

  .card-front .wordmark { left: 52px; top: 146px; color: var(--brand-blue); }
  .card-front .wordmark-square { background: var(--brand-blue); }
  .card-back .wordmark { left: 172px; top: 140px; color: #ffffff; }
  .card-back .wordmark-square { background: #ffffff; }

  .divider {
    position: absolute;
    left: 304px; top: 70px;
    width: 1px; height: 218px;
    background: linear-gradient(to bottom, transparent, var(--rule-grey) 15%, var(--rule-grey) 85%, transparent);
  }
  .contact { position: absolute; left: 329px; top: 68px; color: var(--text-grey); }
  .contact-name {
    font-family: "Open Sans", Arial, sans-serif;
    font-weight: 700;
    font-size: 20px;
    color: var(--brand-blue);
    letter-spacing: 0.3px;
    line-height: 26px;
  }
  .contact-title { font-size: 15px; line-height: 19px; letter-spacing: 0.3px; }
  .contact-license { font-size: 13px; line-height: 19px; margin-bottom: 6px; }
  .contact-address { font-size: 14px; line-height: 17px; font-style: normal; margin-bottom: 10px; }
  .contact-lines { list-style: none; font-size: 14px; }
  .contact-lines li { display: flex; align-items: center; gap: 8px; height: 19px; }
  .contact-lines svg { width: 13px; height: 13px; flex: none; fill: var(--brand-blue); }

  .footer-rule {
    position: absolute; left: 0; right: 0; top: 330px;
    height: 1px; background: var(--rule-grey);
  }
  .footer-band {
    position: absolute; left: 0; right: 0; bottom: 0;
    height: 8px; background: var(--band-blue);
  }
</style>
</head>
<body>
  <section class="card card-front" aria-label="Business card front">
    <div class="wordmark">
      <span class="wordmark-square"></span>
      <span class="wordmark-name"><span class="line-main">BRINDLE OAK</span><span class="line-sub">Mortgage Group</span></span>
    </div>
    <div class="divider"></div>
    <div class="contact">
      <div class="contact-name">DANA WHITLOCK</div>
      <div class="contact-title">Branch Manager</div>
      <div class="contact-license">NMLS# 4827305</div>
      <address class="contact-address">Brindle Oak Mortgage Group<br>14 N. Larkspur, Suite 210<br>Aspen Falls, CO 80921</address>
      <ul class="contact-lines">
        <li><svg viewBox="0 0 16 16"><path d="M3.6 1.2l2.2 2.6c.4.5.3 1.1-.1 1.5L4.6 6.4c.9 2 2.6 3.8 4.8 4.9l1.1-1.1c.4-.4 1.1-.5 1.5-.1l2.6 2.1c.5.4.5 1.1.1 1.5l-1.3 1.3C11.5 16.9 0.8 6.8 2.1 2.5z"/></svg>719-555-0143</li>
        <li><svg viewBox="0 0 16 16"><path d="M4.5 0h7a1.5 1.5 0 0 1 1.5 1.5v13a1.5 1.5 0 0 1-1.5 1.5h-7A1.5 1.5 0 0 1 3 14.5v-13A1.5 1.5 0 0 1 4.5 0zM5 2v10.5h6V2zm3 11.2a.9.9 0 1 0 0 1.8.9.9 0 0 0 0-1.8z"/></svg>719-555-0178</li>
        <li><svg viewBox="0 0 16 16"><path d="M1 3h14v1.2L8 9 1 4.2zM1 5.6l7 4.8 7-4.8V13H1z"/></svg>Dana@BrindleOakLoans.com</li>
        <li><svg viewBox="0 0 16 16"><path d="M8 1a7 7 0 1 0 0 14A7 7 0 0 0 8 1zm-1 2.3c.6.4.3 1.3 1.2 1.6.8.3 1.6-.3 2 .6.3.8-.8 1.2-.6 2 .2.9 1.4.6 1.5 1.6.1.9-.9 2.4-1.8 3-.5-1 .3-2-.6-2.6-.8-.6-2-.2-2.4-1.2-.5-1 .5-1.7-.3-2.4C5.3 5.2 4.4 6 3.6 5.5 4.4 4.3 5.6 3.5 7 3.3z"/></svg>www.BrindleOakLoans.com</li>
      </ul>
    </div>
    <div class="footer-rule"></div>
    <div class="footer-band"></div>
  </section>

  <section class="card card-back" aria-label="Business card back">
    <div class="wordmark">
      <span class="wordmark-square"></span>
      <span class="wordmark-name"><span class="line-main">BRINDLE OAK</span><span class="line-sub">Mortgage Group</span></span>
    </div>
  </section>
</body>
</html>
```